Fernwick Digital Marketing Agency Website Design. I need a new website for my digital marketing agency. It needs to be FAST and easy to use. I want to be able to add videos to the main homepage like this page: https://www.lumatreeweb.example/search-marketing/cleveland-ohio-seo-companyI'd like to have the request quote tab on the top right side as well as my number above it. The following website is my favorite overall: http://www.vantorelgroup.example/ I'd love to copy something like that.

***** Website I want to copy: http://www.vantorelgroup.example/services/ ******
Updates

This needs to be a Wordpress website. Sorry for any confusion as this is the first time using MakerQuill. I need the homepage as described as well as a Services Page and Contact Us page. Services page should be simply yet creative with a spot for me to insert up to 8 services.

Target Market(s)

Business owners

Industry/Entity Type

Digital Marketing

Coding

Coded - Design and coding required

Number of Pages Required

3 page

Font styles to use
Other font styles liked:
• Oswald

Colors

Designer to choose colors to be used in the design.

Requirements
Must have
• I need to have a nice design/template to work off of in Wordpress. It needs to be bright and vibrant yet elegant in design.
Nice to have
• CTA at the top right as well as a place for the phone number. http://www.vantorelgroup.example/services/

```html
<!DOCTYPE html>
<html lang="en">
<head>
<meta charset="utf-8">
<title>Fernwick Digital Marketing — Testimonials</title>
<link href="https://fonts.googleapis.com/css2?family=Oswald:wght@400;500&family=Arimo:wght@400;700&display=swap" rel="stylesheet">
<style>
  :root {
    --orange: #f5a266;
    --orange-deep: #ef8a3e;
    --ink: #3a3a3a;
    --text: #4a4a4a;
    --panel: rgba(245,245,245,0.93);
    --footer: #141414;
    --video: #252525;
    --blue: #3f86e0;
  }
  * { margin: 0; padding: 0; box-sizing: border-box; }
  html, body { width: 1200px; height: 1200px; overflow: hidden; }
  body { position: relative; font-family: "Arimo", Arial, sans-serif; background: #888; }
  .backdrop {
    position: absolute; inset: 0 0 252px 0;
    background: linear-gradient(115deg, #5c5c5c 0%, #9a9a9a 25%, #d8d8d8 45%, #7a7a7a 60%, #b9b9b9 80%, #e8e8e8 100%);
  }
  .panel { position: absolute; left: 0; width: 1200px; background: var(--panel); border-top: 1px solid #8c8c8c; border-bottom: 1px solid #8c8c8c; }
  .testimonials { top: 30px; height: 379px; }
  .message { top: 463px; height: 486px; }
  .tab {
    position: absolute; left: 0; top: 0; width: 524px; height: 47px;
    background: var(--orange); box-shadow: 0 1px 2px rgba(0,0,0,.25);
    font-family: "Oswald", sans-serif; color: #fff; font-size: 29px;
    text-align: right; padding-right: 35px; line-height: 47px;
  }
  .video { position: absolute; left: 256px; top: 102px; width: 406px; height: 247px; background: var(--video); }
  .video-frame { position: absolute; left: 139px; top: 0; width: 126px; height: 221px;
    background: linear-gradient(160deg, #cfcfcf 0%, #8a8a8a 40%, #4a4a4a 75%, #6d6d6d 100%); }
  .video-play { position: absolute; left: 168px; top: 84px; }
  .video-controls { position: absolute; left: 0; bottom: 0; width: 406px; height: 26px; background: #1d1d1d; }
  .video-time { position: absolute; left: 242px; top: 8px; font-size: 8px; color: #ddd; }
  .testimonial-copy { position: absolute; left: 698px; top: 110px; width: 322px; }
  .testimonial-copy h2 { font-family: "Oswald", sans-serif; font-weight: 400; font-size: 24px; line-height: 36px; color: var(--ink); white-space: nowrap; }
  .testimonial-copy h2 span { color: var(--orange-deep); }
  .testimonial-copy p { margin-top: 22px; font-size: 15.6px; line-height: 28.8px; color: var(--text); hyphens: auto; -webkit-hyphens: auto; }
  .message-head { position: absolute; left: 468px; top: 70px; font-family: "Oswald", sans-serif; font-weight: 500; font-size: 32px; line-height: 46px; color: var(--ink); white-space: nowrap; }
  .pin { position: absolute; left: 846px; top: 43px; }
  .message-body { position: absolute; left: 289px; top: 155px; width: 706px; font-size: 15.6px; line-height: 25.6px; color: var(--text); hyphens: auto; -webkit-hyphens: auto; }
  .message-body p { text-indent: 29px; margin-bottom: 25.6px; }
  .message-body strong { color: var(--ink); }
  .message-fade { position: absolute; left: 0; right: 0; bottom: 0; height: 120px; background: #e8e8e8; }
  .footer { position: absolute; left: 0; top: 949px; width: 1200px; height: 251px; background: var(--footer); color: #fff; }
  .footer h3 { position: absolute; top: 52px; font-family: "Oswald", sans-serif; font-weight: 400; font-size: 23px; line-height: 30px; white-space: nowrap; }
  .info-head { left: 459px; }
  .find-head { left: 697px; }
  .address { position: absolute; left: 472px; top: 99px; font-size: 14.5px; line-height: 15px; }
  .contact-row { position: absolute; left: 441px; font-size: 14.5px; display: flex; align-items: center; gap: 11px; }
  .social { position: absolute; left: 725px; top: 89px; width: 38px; height: 38px; border-radius: 50%; background: var(--orange); }
  .copyright { position: absolute; left: 0; width: 1200px; top: 224px; text-align: center; font-size: 14.5px; }
</style>
</head>
<body>
  <div class="backdrop" role="img" aria-label="Black and white photograph of a highway overpass as page background"></div>

  <section class="panel testimonials">
    <div class="tab">TESTIMONIALS</div>
    <div class="video">
      <div class="video-frame" role="img" aria-label="Video still of the client speaking from his car"></div>
      <svg class="video-play" width="70" height="80" viewBox="0 0 70 80"><path d="M4 4 L66 40 L4 76 Z" fill="var(--blue)" opacity=".92"/></svg>
      <div class="video-controls">
        <svg width="406" height="26" viewBox="0 0 406 26">
          <path d="M13 8 L21 13 L13 18 Z" fill="#eee"/>
          <rect x="28" y="10.5" width="204" height="5" rx="2.5" fill="#e6e6e6"/>
          <rect x="28" y="10.5" width="124" height="5" rx="2.5" fill="var(--blue)"/>
          <path d="M290 10 h3 l4 -3 v12 l-4 -3 h-3 z" fill="#eee"/>
          <path d="M299 10 q2 3 0 6" stroke="#eee" fill="none"/>
          <rect x="309" y="11" width="60" height="4" rx="2" fill="#eee"/>
          <rect x="309" y="11" width="42" height="4" rx="2" fill="var(--blue)"/>
          <path d="M382 8 v4 h-4 M388 8 v4 h4 M382 19 v-4 h-4 M388 19 v-4 h4" stroke="#eee" stroke-width="1.5" fill="none"/>
        </svg>
        <span class="video-time">3:15 / 5:00</span>
      </div>
    </div>
    <div class="testimonial-copy">
      <h2>A CUSTOMER’S <span>5 STAR</span> TESTIMONIAL</h2>
      <p>Watch a video testimonial from our client, the owner of one of Cleveland's and Akron's top Electrician Companies!&nbsp; We love local busi&shy;nesses and want yours to grow like his busi&shy;ness!</p>
    </div>
  </section>

  <section class="panel message">
    <div class="message-fade"></div>
    <h2 class="message-head">YOUR MAIN MESSAGE HERE</h2>
    <svg class="pin" width="96" height="98" viewBox="0 0 96 98">
      <ellipse cx="48" cy="80" rx="45" ry="14.5" fill="none" stroke="var(--orange)" stroke-width="4.5"/>
      <line x1="48" y1="30" x2="48" y2="80" stroke="var(--orange)" stroke-width="5" stroke-linecap="round"/>
      <circle cx="48" cy="23" r="22" fill="var(--orange)"/>
    </svg>
    <div class="message-body">
      <p><strong>Use this space to tell people what your company does and why and how it does it.</strong> What are you known for? Who likes you? What's your number one competitive advantage? Include all the things that make your business unique and better than the competition. Do you have a patented 13-step process for taxidermy that results in the most lifelike stuffed owls? You gotta mention that.</p>
      <p>Other good things to weave into this copy include: awards won, distinctions given, number of products sold, company philosophy (just keep it short), interesting company history bits, and any&shy;thing that makes a reader think you'd be awesome to do business with.</p>
    </div>
  </section>

  <footer class="footer">
    <h3 class="info-head">COMPANY INFORMATION</h3>
    <h3 class="find-head">FIND US ON</h3>
    <div class="address">2260 Larchmont Hollow Rd.<br>Brookhaven, OH 44297</div>
    <div class="contact-row" style="top:141px">
      <svg width="20" height="20" viewBox="0 0 20 20"><path d="M4 1 L8 5 L6 8 Q8 12 12 14 L15 12 L19 16 L16 19 Q8 19 3 12 Q0 7 1 4 Z" fill="var(--orange)"/></svg>
      <span>440-555-0184</span>
    </div>
    <div class="contact-row" style="top:170px">
      <svg width="20" height="16" viewBox="0 0 20 16"><rect x="1" y="1" width="18" height="14" fill="none" stroke="var(--orange)" stroke-width="2"/><path d="M1 1 L10 9 L19 1 M1 15 L8 8 M19 15 L12 8" stroke="var(--orange)" stroke-width="2" fill="none"/></svg>
      <span>fernwickllc@mailbox.example</span>
    </div>
    <div class="social" role="img" aria-label="Social media profile link"></div>
    <div class="copyright">Copyright © 2019 Fernwick Digital Marketing Company Privacy Policy</div>
  </footer>
</body>
</html>
```